Packaging design for Solmara Ridge Premium Extra Virgin Olive Oil

Based on our label design, we need a whole packaging design for our product, which includes bottle and gift pack design.

Ideally we prefer the shape of Tovena bottle, please refer to the picture that I uploaded. With cork or screw neck finish, bottle must be in antique green, dark green or amber colour. However, any other ideas will be appreciated, as long as it looks great.

The gift pack design is quite open, personally I prefer the paper tube package. we uploaded some sample designs that we like for your reference. Please feel free to use the actual logos and barcode for our product attached in brief files.

For practical reason, we prefer to use 250ml Tovena glass bottle, please see the dimention details below, regarding to the bottle shape please refer to my sample picture.
Capacity: 250 ml
Weight: 250 grs
Diameter: 54,10 mm
Height: 250,80 mm

Requirements
Must have
• Solmara Ridge Olive Oil Logo.
"Fall 2014 Harvest"
Barcode
Product of Australia Logo
Kestrel Pure Press Certified Logo

```html
<!DOCTYPE html>
<html lang="en">
<head>
<meta charset="utf-8">
<title>Solmara Ridge – Dieline Proposal</title>
<link rel="stylesheet" href="https://fonts.googleapis.com/css2?family=Cormorant+Garamond:ital,wght@0,500;1,500&family=Great+Vibes&family=PT+Sans:wght@400;700&display=swap">
<style>
  :root {
    --bg: #000000;
    --accent: #1ea7d6;
    --cream-light: #f8f3df;
    --cream-dark: #e6dcb2;
    --olive-dark: #2f5a39;
    --olive-mid: #4f7d5c;
    --olive-deep: #3c6a48;
    --olive-light: #6a9475;
    --gold: #d8c46a;
    --white: #ffffff;
  }
  html, body {
    margin: 0;
    padding: 0;
    width: 909px;
    height: 1200px;
    overflow: hidden;
    background: var(--bg);
  }
  .dieline { display: block; width: 909px; height: 1200px; }
  .title { font-family: "PT Sans", sans-serif; font-size: 30px; fill: var(--accent); }
  .dimension-text { font-family: "PT Sans", sans-serif; font-size: 35px; fill: var(--accent); }
  .dimension-text--small { font-size: 27px; }
  .dimension-line { stroke: var(--accent); stroke-width: 1.4; fill: none; }
  .guide-line { stroke: var(--accent); stroke-width: 1; stroke-dasharray: 3 3; fill: none; opacity: .8; }
  .cap-tooth, .cap-disc { stroke: var(--accent); stroke-width: 1.5; }
  .cap--top .cap-tooth, .cap--top .cap-disc { fill: url(#creamFill); }
  .cap--bottom .cap-tooth, .cap--bottom .cap-disc { fill: var(--olive-mid); }
  .cap-name { font-family: "PT Sans", sans-serif; font-size: 32px; fill: var(--accent); text-anchor: middle; }
  .cap-note { font-family: "PT Sans", sans-serif; font-size: 10px; fill: var(--accent); text-anchor: middle; }
  .cap-rule { stroke: #8a8a7a; stroke-width: .8; stroke-dasharray: 2 2; }
  .label-front { fill: url(#creamFill); stroke: var(--accent); stroke-width: 1.2; }
  .label-back { stroke: var(--accent); stroke-width: 1.2; }
  .label-heading { font-family: "Cormorant Garamond", serif; fill: var(--olive-dark); }
  .label-heading--main { font-size: 25px; letter-spacing: .5px; }
  .label-heading--sub { font-size: 16px; letter-spacing: 1px; }
  .label-copy { font-family: "PT Sans", sans-serif; font-weight: 700; font-size: 7.4px; fill: var(--olive-dark); text-anchor: middle; }
  .brand-name { font-family: "Cormorant Garamond", serif; font-size: 15px; fill: var(--olive-dark); }
  .harvest-script { font-family: "Great Vibes", cursive; font-size: 28px; fill: var(--white); text-anchor: middle; }
  .harvest-year { font-family: "Cormorant Garamond", serif; font-style: italic; font-size: 30px; fill: var(--white); text-anchor: middle; }
  .label-fineprint { font-family: "PT Sans", sans-serif; font-size: 6px; fill: #d9e6dc; }
</style>
</head>
<body>
<svg class="dieline" viewBox="0 0 909 1200" xmlns="http://www.w3.org/2000/svg">
  <defs>
    <linearGradient id="creamFill" x1="0" y1="0" x2="1" y2="1">
      <stop offset="0" stop-color="var(--cream-light)"/>
      <stop offset="1" stop-color="var(--cream-dark)"/>
    </linearGradient>
    <linearGradient id="groveFill" x1="0" y1="0" x2="1" y2="1">
      <stop offset="0" stop-color="var(--olive-light)"/>
      <stop offset=".5" stop-color="var(--olive-mid)"/>
      <stop offset="1" stop-color="var(--olive-deep)"/>
    </linearGradient>
    <rect id="tooth" class="cap-tooth" x="-16" y="-99" width="32" height="46" rx="2"/>
  </defs>

  <text class="title" x="14" y="44">DIELINE proposal</text>

  <!-- Top cap -->
  <g class="cap cap--top" transform="translate(511 148)">
    <use href="#tooth"/><use href="#tooth" transform="rotate(30)"/><use href="#tooth" transform="rotate(60)"/>
    <use href="#tooth" transform="rotate(90)"/><use href="#tooth" transform="rotate(120)"/><use href="#tooth" transform="rotate(150)"/>
    <use href="#tooth" transform="rotate(180)"/><use href="#tooth" transform="rotate(210)"/><use href="#tooth" transform="rotate(240)"/>
    <use href="#tooth" transform="rotate(270)"/><use href="#tooth" transform="rotate(300)"/><use href="#tooth" transform="rotate(330)"/>
    <circle class="cap-disc" r="68"/>
    <text class="cap-name" y="-16">Top</text>
    <text class="cap-note" y="5">diameter:</text>
    <line class="cap-rule" x1="-58" y1="11" x2="58" y2="11"/>
    <text class="cap-note" y="23">3 inches</text>
  </g>

  <!-- Front label -->
  <g class="label label--front">
    <rect class="label-front" x="287" y="239" width="317" height="213"/>
    <text class="label-heading label-heading--main" x="312" y="279">PREMIUM</text>
    <text class="label-heading label-heading--sub" x="313" y="299">EXTRA VIRGIN</text>
    <text class="label-copy">
      <tspan x="383" y="318">Nestled in the Greater Bendigo region of</tspan>
      <tspan x="383" y="329">Victoria, Solmara Ridge represents one of</tspan>
      <tspan x="383" y="340">the freshest and finest extra virgin olive oils in</tspan>
      <tspan x="383" y="351">Australia. Blessed by Central Victoria's</tspan>
      <tspan x="383" y="362">Mediterranean climate, our extra virgin olive</tspan>
      <tspan x="383" y="373">oils feature a crisp, distinctive taste of</tspan>
      <tspan x="383" y="384">freshness and fruity aromas.</tspan>
    </text>
    <g class="brand-mark">
      <circle cx="490" cy="299" r="8" fill="var(--olive-dark)"/>
      <text class="brand-name" x="503" y="304">Solmara Ridge</text>
    </g>
    <circle class="badge badge--origin" cx="341" cy="427" r="14" fill="var(--gold)" role="img" aria-label="Product of Australia badge"/>
    <rect class="badge badge--certified" x="378" y="412" width="28" height="28" fill="var(--olive-dark)" role="img" aria-label="Kestrel Pure Press Certified badge"/>
    <path class="label-cutout" role="img" aria-label="Leaf-shaped window cutout" fill="var(--white)"
          d="M530 366 C506 398 497 428 504 452 L546 452 C550 424 524 404 530 366 Z"/>
  </g>

  <!-- Height dimension, front label -->
  <text class="dimension-text" x="17" y="345">4.02 inches</text>
  <line class="dimension-line" x1="231" y1="239" x2="231" y2="452"/>
  <line class="dimension-line" x1="219" y1="239" x2="243" y2="239"/>
  <line class="dimension-line" x1="219" y1="452" x2="243" y2="452"/>
  <line class="guide-line" x1="243" y1="239" x2="287" y2="239"/>
  <line class="guide-line" x1="243" y1="452" x2="287" y2="452"/>

  <!-- Width dimension -->
  <line class="guide-line" x1="287" y1="452" x2="287" y2="545"/>
  <line class="guide-line" x1="604" y1="452" x2="604" y2="545"/>
  <text class="dimension-text dimension-text--small" x="312" y="515">6 inches wide</text>
  <line class="dimension-line" x1="287" y1="533" x2="604" y2="533"/>
  <line class="dimension-line" x1="287" y1="525" x2="287" y2="541"/>
  <line class="dimension-line" x1="604" y1="525" x2="604" y2="541"/>

  <!-- Back label -->
  <g class="label label--back">
    <rect class="label-back" x="287" y="650" width="317" height="309" fill="url(#groveFill)" role="img" aria-label="Olive tree grove illustration in green tones"/>
    <text class="harvest-script" x="527" y="750">Fall Harvest</text>
    <text class="harvest-year" x="527" y="780">2014</text>
    <text class="label-fineprint" x="463" y="953">© 2014 Solmara Ridge Olive Oil. All rights reserved.</text>
  </g>
  <ellipse class="leaf-tab" role="img" aria-label="Olive leaf illustration tab" cx="529" cy="625" rx="22" ry="57"
           transform="rotate(12 529 625)" fill="var(--cream-light)" stroke="var(--olive-mid)" stroke-width="3"/>

  <!-- Height dimension, back label -->
  <line class="guide-line" x1="604" y1="650" x2="681" y2="650"/>
  <line class="guide-line" x1="604" y1="959" x2="681" y2="959"/>
  <line class="dimension-line" x1="681" y1="650" x2="681" y2="959"/>
  <line class="dimension-line" x1="669" y1="650" x2="693" y2="650"/>
  <line class="dimension-line" x1="669" y1="959" x2="693" y2="959"/>
  <text class="dimension-text" x="712" y="826">5.8 inches</text>

  <!-- Bottom cap -->
  <g class="cap cap--bottom" transform="translate(511 1052)">
    <use href="#tooth"/><use href="#tooth" transform="rotate(30)"/><use href="#tooth" transform="rotate(60)"/>
    <use href="#tooth" transform="rotate(90)"/><use href="#tooth" transform="rotate(120)"/><use href="#tooth" transform="rotate(150)"/>
    <use href="#tooth" transform="rotate(180)"/><use href="#tooth" transform="rotate(210)"/><use href="#tooth" transform="rotate(240)"/>
    <use href="#tooth" transform="rotate(270)"/><use href="#tooth" transform="rotate(300)"/><use href="#tooth" transform="rotate(330)"/>
    <circle class="cap-disc" r="68"/>
    <text class="cap-name" y="-38">Bottom</text>
    <text class="cap-note" y="-17">diameter:</text>
    <line class="cap-rule" x1="-58" y1="-11" x2="58" y2="-11"/>
    <text class="cap-note" y="0">3 inches</text>
  </g>
</svg>
</body>
</html>
```